Bright Prospect Hub

I would like 4 different size banner ads. The "Standard" online sizes. I believe they are: 125x125 | 728x90 | 468x60 | 250x250 These banners will be for promoting the website. I want to make sure you can read what the banners say so NO real fancy text. I've uploaded a few ideas as I do want them to kinda look like the website. https://www.brightprospecthub.com/ Take a look at the site and you will see we use money bags, dollar signs and bright colors.

```html
<!DOCTYPE html>
<html lang="en">
<head>
<meta charset="utf-8">
<title>Bright Prospect Hub – Banner Set</title>
<link href="https://fonts.googleapis.com/css2?family=Anton&family=Inter:wght@400&family=Playfair+Display:ital,wght@1,700&display=swap" rel="stylesheet">
<style>
:root{
  --stage:#232323;
  --label:#ffffff;
  --navy:#3a4bbf;
  --ink:#000000;
  --deep:#050a2a;
  --flare:#ffb21e;
  --gold-1:#f6c21c;
  --gold-2:#fff3c0;
  --gold-3:#c9a24a;
  --sky-1:#8ee4f5;
  --sky-2:#1f7fd1;
  --sky-3:#0a5fb8;
  --red:#e0182a;
  --coin-1:#ffe27a;
  --coin-2:#d9a015;
}
*{margin:0;padding:0;box-sizing:border-box}
html,body{width:1200px;height:903px;overflow:hidden;background:var(--stage)}
.canvas{position:relative;width:1200px;height:903px;font-family:"Anton",sans-serif}
.size-label{position:absolute;font-family:"Inter",sans-serif;color:var(--label);font-size:23px;line-height:1;transform:translateY(-50%)}

.banner{position:absolute;overflow:hidden;box-shadow:0 10px 18px rgba(0,0,0,.55);
  background:
   radial-gradient(ellipse 45% 45% at 100% 100%, var(--flare) 0%, rgba(255,178,30,.35) 30%, rgba(0,0,0,0) 70%),
   radial-gradient(ellipse 90% 80% at 0% 0%, var(--navy) 0%, rgba(20,40,90,.6) 40%, rgba(0,0,0,0) 80%),
   radial-gradient(ellipse 80% 60% at 50% 100%, #0a0f6a 0%, rgba(0,0,0,0) 80%),
   var(--ink);}
.txt{position:absolute;left:0;right:0;text-align:center;line-height:1;text-transform:uppercase;white-space:nowrap}
.gold{background:linear-gradient(100deg,var(--gold-1) 0%,var(--gold-3) 40%,var(--gold-2) 65%,var(--gold-1) 100%);-webkit-background-clip:text;background-clip:text;color:transparent}
.sky{background:linear-gradient(100deg,var(--sky-1) 0%,var(--sky-2) 60%,var(--sky-3) 100%);-webkit-background-clip:text;background-clip:text;color:transparent}
.coin{position:absolute;border-radius:50%;background:radial-gradient(circle at 40% 35%,var(--coin-1),var(--coin-2) 70%,#8a5a05)}
.hand{position:absolute;background:linear-gradient(90deg,#7fdcf2,#2f98d6);border-radius:30px 60px 40px 20px}
svg{position:absolute;overflow:visible}

/* 125 */
.banner-125{left:387px;top:76px;width:261px;height:261px}
.banner-125 .l1{top:36px;font-size:39px;letter-spacing:-.5px}
.banner-125 .l2{top:77px;font-size:27px;letter-spacing:-.3px}
.banner-125 .l3{top:102px;font-size:62px;letter-spacing:-1px}
.banner-125 .l4{top:158px;font-size:70px;letter-spacing:-1px}

/* 250 */
.banner-250{left:671px;top:76px;width:456px;height:456px}
.banner-250 .l1{top:55px;font-size:55px}
.banner-250 .l2{top:107px;font-size:160px;letter-spacing:-2px}
.banner-250 .rule{position:absolute;top:276px;height:1px;width:140px;background:rgba(255,255,255,.6)}
.banner-250 .dollar{position:absolute;top:256px;left:0;right:0;text-align:center;color:#fff;font-size:36px;line-height:1}
.banner-250 .l3{top:300px;font-size:52px}
.banner-250 .l4{top:350px;font-size:52px;letter-spacing:-.5px}

/* 468 */
.banner-468{left:581px;top:591px;width:545px;height:93px}
.banner-468 .l1{left:135px;right:auto;top:15px;font-size:38px;letter-spacing:-.5px}
.banner-468 .l2{left:162px;right:auto;top:56px;font-size:21px;letter-spacing:.5px}

/* 728 */
.banner-728{left:73px;top:701px;width:1054px;height:131px}
.banner-728 .l1{left:197px;right:auto;top:13px;font-size:58px;text-align:left}
.banner-728 .l2{left:197px;right:auto;top:61px;font-size:58px;text-align:left;letter-spacing:-.5px}
.banner-728 .tagline{position:absolute;left:622px;top:36px;font-family:"Playfair Display",serif;font-style:italic;font-weight:700;color:#fff;font-size:28px;line-height:30px;white-space:nowrap}
</style>
</head>
<body>
<div class="canvas">

  <span class="size-label" style="left:153px;top:212px">125 PX x 125 PX</span>
  <span class="size-label" style="left:478px;top:491px">250px X 250px</span>
  <span class="size-label" style="left:443px;top:640px">468 X 60px</span>
  <span class="size-label" style="left:81px;top:670px">728x90px</span>

  <!-- 125 x 125 -->
  <section class="banner banner-125">
    <svg width="261" height="261" viewBox="0 0 261 261">
      <g fill="#d9a530">
        <rect x="218" y="30" width="8" height="14"/><rect x="229" y="24" width="8" height="20"/>
        <rect x="240" y="16" width="8" height="28"/><rect x="251" y="8" width="8" height="36"/>
        <rect x="214" y="44" width="47" height="3"/>
      </g>
      <polyline points="218,20 232,16 250,4" fill="none" stroke="#e8c35a" stroke-width="1.5"/>
      <polyline points="160,244 200,222 250,194" fill="none" stroke="#2a4f8a" stroke-width="2"/>
    </svg>
    <div class="txt l1 sky">Welcome to</div>
    <div class="txt l2 gold">Truely Unlimited</div>
    <div class="txt l3 sky">Ongoing</div>
    <div class="txt l4 gold">Income</div>
    <div class="coin" role="img" aria-label="Stack of gold coins" style="left:8px;top:214px;width:48px;height:42px"></div>
  </section>

  <!-- 250 x 250 -->
  <section class="banner banner-250">
    <svg width="456" height="456" viewBox="0 0 456 456">
      <g fill="rgba(90,110,130,.18)">
        <rect x="280" y="100" width="40" height="140"/><rect x="330" y="60" width="40" height="180"/>
        <rect x="380" y="30" width="40" height="210"/><rect x="420" y="10" width="36" height="230"/>
      </g>
      <polyline points="250,110 340,50 432,6" fill="none" stroke="rgba(110,130,150,.35)" stroke-width="3"/>
    </svg>
    <div class="txt l1 gold">Bright Prospect</div>
    <div class="txt l2 gold">Hub</div>
    <div class="rule" style="left:66px"></div>
    <div class="rule" style="right:66px"></div>
    <div class="dollar">$</div>
    <div class="txt l3 sky">Plus, a monthly</div>
    <div class="txt l4 sky">Residual income!</div>
  </section>

  <!-- 468 x 60 -->
  <section class="banner banner-468">
    <div class="coin" role="img" aria-label="Stack of gold coins" style="left:25px;top:2px;width:78px;height:78px"></div>
    <div class="txt l1 gold">Leads, leads, leads...</div>
    <div class="txt l2 sky">Unlimited growing income</div>
    <svg width="545" height="93" viewBox="0 0 545 93">
      <g fill="#f2c323">
        <rect x="434" y="68" width="14" height="10"/><rect x="452" y="58" width="14" height="20"/>
        <rect x="470" y="48" width="14" height="30"/><rect x="488" y="38" width="14" height="40"/>
        <rect x="506" y="24" width="14" height="54"/><rect x="422" y="78" width="102" height="4"/>
      </g>
      <polyline points="436,50 470,34 486,38 512,12" fill="none" stroke="#f2c323" stroke-width="2"/>
      <polygon points="512,12 506,13 510,17" fill="#f2c323" stroke="#f2c323" stroke-width="2"/>
    </svg>
  </section>

  <!-- 728 x 90 -->
  <section class="banner banner-728">
    <div class="hand" role="img" aria-label="Pointing hand illustration" style="left:0;top:26px;width:183px;height:89px"></div>
    <div class="txt l1 gold">Get all the</div>
    <div class="txt l2 gold">Leads you want</div>
    <svg width="1054" height="131" viewBox="0 0 1054 131">
      <path d="M514 86 C560 90 590 80 612 60" fill="none" stroke="var(--red)" stroke-width="3"/>
      <polyline points="598,58 614,57 610,72" fill="none" stroke="var(--red)" stroke-width="3"/>
      <g fill="#1f8fd6">
        <rect x="898" y="86" width="18" height="20"/><rect x="922" y="72" width="18" height="34"/>
        <rect x="946" y="58" width="18" height="48"/><rect x="970" y="42" width="18" height="64"/>
        <rect x="994" y="22" width="18" height="84"/><rect x="880" y="106" width="140" height="7"/>
      </g>
      <polyline points="900,66 952,40 966,44 1010,6" fill="none" stroke="#1f8fd6" stroke-width="3"/>
      <polygon points="1012,4 1002,6 1008,13" fill="#1f8fd6"/>
    </svg>
    <div class="tagline">Truly Unlimited<br>Ongoing Income</div>
    <div class="coin" role="img" aria-label="Stack of gold coins" style="left:860px;top:24px;width:48px;height:45px"></div>
  </section>

</div>
</body>
</html>
```